Bright Path Flyer Design for Virtual Online Clinic. -5.5 x 8.5 inches (half sheet)

We need a clean, modern flyer design for Bright Path, a new virtual walk-in clinic based in British Columbia. The flyer will be used in libraries, pharmacies, and community centers to help residents easily access primary care through their Bright Path NFC access card.
The flyer will ask a question : NEED A DOCTOR? This should be large and attention grabbing.
The design should clearly feature a Bright Path card image (the access card) as the centerpiece and visually show how patients can use it to book appointments. The tone should feel trustworthy, healthcare-oriented, and community-friendly — clean fonts, clear spacing, and strong readability from a distance.

Side One: This card has the NFC Access Card.
NEED A DOCTOR? (Large Font, Attention Grabbing)
How to Book an Appointment using your Bright Path Card
Step 1: Tap Your Card on Your Phone
Hold your card near the back of your phone.
It will activate automatically — no app needed.
The Bright Path scheduler will open.
Step 2: Schedule Your Appointment
Select your clinical concern.
Choose your time window.
Register (only once).
Confirm your appointment.
Step 3: Relax, we’ll take care of the rest
A doctor will call during your scheduled time.
Once booked, you’ll be able to call our office.
No emails, no texts — just a real person.
It’s that simple.
Side Two:
About Bright Path
Created by Dr. Marcus Ferrigan
Bright Path was founded to make healthcare simple and convenient. Prescription renewals. Common infections. Medical notes. And so much more.
Our doctors can address 120+ health concerns virtually — providing quality care without the waiting room. No waiting rooms. Just real doctors providing real care.
Why Patients Choose Bright Path
Easy access – book and be seen from anywhere in BC.
Effortless booking – tap your Bright Path Card to begin.
Trusted physicians – every visit is with a licensed BC family doctor.
How It Works
Book your visit — choose a time window that fits your day.
Join the queue — you’ll be called when it’s your turn.
Speak directly with your doctor — simple, secure, and stress-free.
Convenient Care for Common Concerns

Additional Details.
Please find the domain to be launched soon. I've attached the NFC card file for review, it is 85.5 mm x 54 mm. The card will be glued to the flyer.
I've attached examples of flyers but they are not the look I am seeking and I am looking for creative solutions.
Thank you!
http://brightpath-example.test/

Adult Patients in British Columbia

Healthcare

• Looking for clean lines, uniform appearance, and high legibility i.e poppins

0054AA
0677BA
7BADD7
CADEEF
E8F1F8

• Need A Doctor?
• Elegant style, not too busy, clear layout.
• Clutter, look cheap - review examples.

```html
<!DOCTYPE html>
<html lang="en">
<head>
<meta charset="utf-8">
<title>Bright Path Flyer</title>
<link rel="stylesheet" href="https://fonts.googleapis.com/css2?family=Montserrat:ital,wght@0,400;0,500;0,600;0,700;0,800;1,600&display=swap">
<style>
  :root {
    --brand-blue: #2b4691;
    --brand-blue-deep: #213a7c;
    --sky: #7badd7;
    --mist: #cadeef;
    --frost: #e8f1f8;
    --white: #ffffff;
    --ink: #1c1c1c;
    --page: #eeeeee;
  }
  * { box-sizing: border-box; margin: 0; padding: 0; }
  html, body { width: 1200px; height: 1200px; overflow: hidden; }
  body {
    background: var(--page);
    font-family: "Montserrat", sans-serif;
    position: relative;
  }
  .flyer {
    position: absolute;
    top: 188px;
    width: 533px;
    height: 822px;
    overflow: hidden;
    background: var(--brand-blue);
  }
  .flyer--front { left: 48px; }
  .flyer--back { left: 618px; }

  .brand-name {
    position: absolute;
    font-weight: 500;
    font-size: 26px;
    letter-spacing: 0.5px;
    z-index: 3;
  }

  /* Front */
  .front-top {
    position: absolute; left: 0; top: 0; width: 100%; height: 356px;
    background: var(--white);
  }
  .flyer--front .brand-name { left: 40px; top: 82px; color: var(--brand-blue); }
  .bird-art {
    position: absolute; left: 250px; top: 10px; width: 275px; height: 390px;
    background: linear-gradient(160deg, var(--frost) 0%, var(--mist) 55%, var(--sky) 100%);
    border-radius: 140px 20px 120px 20px;
    opacity: 0.85;
    z-index: 1;
  }
  .headline {
    position: absolute; left: 40px; top: 226px; z-index: 3;
    color: var(--brand-blue); font-weight: 800; line-height: 1;
  }
  .headline__big { display: block; font-size: 78px; letter-spacing: 1px; }
  .headline__small { display: block; font-size: 44px; margin-top: 6px; }
  .booking-title {
    position: absolute; left: 40px; top: 412px; z-index: 3;
    color: var(--white); font-weight: 600; font-size: 24px; line-height: 1.22;
  }
  .front-base {
    position: absolute; left: 0; bottom: 0; width: 100%; height: 66px;
    background: var(--brand-blue-deep);
    z-index: 1;
  }
  .steps { position: absolute; left: 0; top: 545px; width: 100%; height: 240px; z-index: 2; }
  .step {
    position: absolute; top: 0; text-align: center; color: var(--white);
    width: 140px; font-size: 11px; line-height: 1.22;
  }
  .step--one { left: 52px; }
  .step--two {
    left: 198px; height: 222px; padding: 0 6px;
    background: var(--white); color: var(--ink);
    border-radius: 24px 4px 24px 4px;
    box-shadow: 5px 6px 0 var(--brand-blue-deep), 4px 8px 12px rgba(0,0,0,0.25);
  }
  .step--three { left: 346px; }
  .step__label { font-weight: 700; font-size: 16px; letter-spacing: 0.5px; margin: 14px 0 12px; }
  .step__lead { font-weight: 700; font-size: 10.5px; margin-bottom: 12px; line-height: 1.25; }
  .step__text p + p { margin-top: 10px; }

  /* Back */
  .back-art {
    position: absolute; left: 0; top: 0; width: 275px; height: 300px;
    background: linear-gradient(150deg, var(--white) 0%, var(--frost) 60%, var(--mist) 100%);
    border-radius: 0 0 160px 0;
  }
  .flyer--back .brand-name { left: 302px; top: 312px; color: var(--white); font-size: 24px; }
  .about { position: absolute; left: 33px; top: 405px; width: 470px; color: var(--white); }
  .about__title { font-weight: 700; font-size: 27px; line-height: 1.1; }
  .about__byline { font-weight: 600; font-style: italic; font-size: 14px; margin-top: 2px; }
  .about__copy { font-size: 12.6px; line-height: 1.3; margin-top: 14px; }
  .about__copy p + p { margin-top: 15px; }
  .about__heading { font-weight: 700; font-size: 17px; margin-top: 20px; }
  .ticks { list-style: none; font-size: 12.6px; line-height: 1.3; margin-top: 4px; }
  .ticks li { display: flex; align-items: center; gap: 4px; }
  .ticks svg { flex: none; width: 10px; height: 10px; }
</style>
</head>
<body>

<section class="flyer flyer--front">
  <div class="front-top"></div>
  <div class="bird-art" role="img" aria-label="Outlined hummingbird illustration in flight"></div>
  <div class="brand-name">Bright Path</div>
  <h1 class="headline">
    <span class="headline__big">NEED</span>
    <span class="headline__small">A DOCTOR?</span>
  </h1>
  <h2 class="booking-title">How to Book<br>an Appointment using<br>your Bright Path Card</h2>

  <div class="front-base"></div>
  <div class="steps">
    <div class="step step--one">
      <div class="step__label">STEP 1</div>
      <div class="step__lead">Tap Your Card<br>on Your Phone</div>
      <div class="step__text">
        <p>Hold your card near the<br>back of your phone.</p>
        <p>It will activate<br>automatically — no app<br>needed.<br>The Bright Path<br>scheduler will open.</p>
      </div>
    </div>
    <div class="step step--two">
      <div class="step__label">STEP 2</div>
      <div class="step__lead">Schedule<br>Your Appointment</div>
      <div class="step__text">
        <p>Select your clinical<br>concern.<br>Choose your time<br>window.</p>
        <p>Register (only once).<br>Confirm your<br>appointment.</p>
      </div>
    </div>
    <div class="step step--three">
      <div class="step__label">STEP 3</div>
      <div class="step__lead">Relax, we’ll take<br>care of the rest</div>
      <div class="step__text">
        <p>A doctor will call during<br>your scheduled time.<br>Once booked, you’ll be<br>able to call our office.<br>No emails, no texts —<br>just a real person.<br>It’s that simple.</p>
      </div>
    </div>
  </div>
</section>

<section class="flyer flyer--back">
  <div class="back-art" role="img" aria-label="Large hummingbird silhouette decoration"></div>
  <div class="brand-name">Bright Path</div>
  <div class="about">
    <h2 class="about__title">About Bright Path</h2>
    <div class="about__byline">Created by Dr. Marcus Ferrigan</div>
    <div class="about__copy">
      <p>Bright Path was founded to make healthcare simple and convenient. Prescription renewals. Common infections. Medical notes. And so much more.</p>
      <p>Our doctors can address 120+ health concerns virtually — providing quality care without the waiting room. No waiting rooms. Just real doctors providing real care.</p>
    </div>
    <h3 class="about__heading">Why Patients Choose Bright Path</h3>
    <ul class="ticks">
      <li><svg viewBox="0 0 10 10"><path d="M1 5.5 L4 8.5 L9 1.5" fill="none" stroke="#fff" stroke-width="1.6"/></svg>Easy access – book and be seen from anywhere in BC.</li>
      <li><svg viewBox="0 0 10 10"><path d="M1 5.5 L4 8.5 L9 1.5" fill="none" stroke="#fff" stroke-width="1.6"/></svg>Effortless booking – tap your Bright Path Card to begin.</li>
      <li><svg viewBox="0 0 10 10"><path d="M1 5.5 L4 8.5 L9 1.5" fill="none" stroke="#fff" stroke-width="1.6"/></svg>Trusted physicians – every visit is with a licensed BC family doctor.</li>
    </ul>
    <h3 class="about__heading">How It Works</h3>
    <ul class="ticks">
      <li><svg viewBox="0 0 10 10"><path d="M1 5.5 L4 8.5 L9 1.5" fill="none" stroke="#fff" stroke-width="1.6"/></svg>Book your visit — choose a time window that fits your day.</li>
      <li><svg viewBox="0 0 10 10"><path d="M1 5.5 L4 8.5 L9 1.5" fill="none" stroke="#fff" stroke-width="1.6"/></svg>Join the queue — you’ll be called when it’s your turn.</li>
      <li><svg viewBox="0 0 10 10"><path d="M1 5.5 L4 8.5 L9 1.5" fill="none" stroke="#fff" stroke-width="1.6"/></svg>Speak directly with your doctor — simple, secure, and stress-free.</li>
      <li><svg viewBox="0 0 10 10"><path d="M1 5.5 L4 8.5 L9 1.5" fill="none" stroke="#fff" stroke-width="1.6"/></svg>Convenient Care for Common Concerns</li>
    </ul>
  </div>
</section>

</body>
</html>
```